LumaMove In-home Personal Training

I would like to have some eye-catching business card design. Opened to any ideas.

The business idea: mobile fitness - train clients at their places

Target Market(s)

General population, 20-60 years old

Industry/Entity Type

Fitness

Contact Information for Business Card

The information to include:
Name: Marta
Call or text: 306-555-0187
Website: LumaMove.ca
Please use the attached logo

Requirements
Should not have
• No orange or purple colours please

```html
<!DOCTYPE html>
<html lang="en">
<head>
<meta charset="utf-8">
<title>LumaMove Business Card</title>
<link rel="stylesheet" href="https://fonts.googleapis.com/css2?family=Montserrat:wght@400;500&display=swap">
<style>
  :root {
    --page-bg: #e6e6e6;
    --card-white: #ffffff;
    --card-black: #111111;
    --swoosh-grey: #4a4a4a;
    --ink: #161616;
    --ink-soft: #333333;
  }
  * { margin: 0; padding: 0; box-sizing: border-box; }
  html, body {
    width: 1200px;
    height: 900px;
    overflow: hidden;
    background: var(--page-bg);
    font-family: "Montserrat", Arial, sans-serif;
    color: var(--ink);
  }
  .sheet {
    position: relative;
    width: 1200px;
    height: 900px;
  }
  .card {
    position: absolute;
    left: 260px;
    width: 680px;
    height: 388px;
    border-radius: 24px;
    overflow: hidden;
    background: var(--card-white);
    box-shadow: 0 6px 18px rgba(0,0,0,0.18);
  }
  .card--front { top: 50px; }
  .card--back { top: 462px; }
  .card__shapes {
    position: absolute;
    inset: 0;
    width: 100%;
    height: 100%;
  }
  .shape-black { fill: var(--card-black); }
  .shape-grey { fill: var(--swoosh-grey); }

  .brand {
    position: absolute;
    display: flex;
    flex-direction: column;
  }
  .brand__row {
    display: flex;
    align-items: center;
  }
  .brand__mark {
    border: 2px solid var(--ink);
    border-radius: 4px;
  }
  .brand__name {
    font-weight: 400;
    letter-spacing: 0.12em;
    color: var(--ink);
    line-height: 1;
  }
  .brand__tagline {
    font-weight: 500;
    text-transform: uppercase;
    color: var(--ink-soft);
    white-space: nowrap;
  }

  .card--front .brand { left: 150px; top: 118px; }
  .card--front .brand__mark { width: 46px; height: 46px; margin-right: 18px; }
  .card--front .brand__name { font-size: 58px; }
  .card--front .brand__tagline { font-size: 12px; letter-spacing: 0.32em; margin: 8px 0 0 66px; }

  .card--back .brand { left: 46px; top: 34px; }
  .card--back .brand__mark { width: 30px; height: 30px; margin-right: 12px; }
  .card--back .brand__name { font-size: 36px; }
  .card--back .brand__tagline { font-size: 8px; letter-spacing: 0.3em; margin: 5px 0 0 42px; }

  .contact {
    position: absolute;
    left: 48px;
    top: 138px;
    list-style: none;
    font-size: 17px;
    font-weight: 400;
    color: var(--ink);
  }
  .contact__item {
    display: flex;
    align-items: center;
    margin-bottom: 14px;
  }
  .contact__icon {
    width: 18px;
    height: 18px;
    margin-right: 16px;
    flex: none;
  }
  .holder-name {
    position: absolute;
    left: 500px;
    top: 196px;
    font-size: 34px;
    font-weight: 500;
    color: var(--ink);
    padding-bottom: 4px;
    border-bottom: 2px solid var(--ink);
    line-height: 1.1;
  }
</style>
</head>
<body>
<main class="sheet">

  <section class="card card--front" aria-label="Business card front">
    <svg class="card__shapes" viewBox="0 0 680 388" aria-hidden="true">
      <path class="shape-black" d="M0,0 H100 C48,60 22,120 0,190 Z"/>
      <path class="shape-grey" d="M44,36 C58,140 150,220 320,262 C170,205 96,130 74,36 Z"/>
      <path class="shape-black" d="M0,268 C210,310 440,262 680,142 V388 H0 Z"/>
    </svg>
    <div class="brand">
      <div class="brand__row">
        <span class="brand__mark"></span>
        <span class="brand__name">LumaMove</span>
      </div>
      <span class="brand__tagline">In-home Personal Training</span>
    </div>
  </section>

  <section class="card card--back" aria-label="Business card back">
    <svg class="card__shapes" viewBox="0 0 680 388" aria-hidden="true">
      <path class="shape-black" d="M400,0 H680 V96 C610,52 520,18 400,0 Z"/>
      <path class="shape-black" d="M0,268 C230,262 440,310 560,388 H0 Z"/>
      <path class="shape-grey" d="M390,294 C490,292 590,322 660,388 H640 C570,338 480,308 390,294 Z"/>
    </svg>
    <div class="brand">
      <div class="brand__row">
        <span class="brand__mark"></span>
        <span class="brand__name">LumaMove</span>
      </div>
      <span class="brand__tagline">In-home Personal Training</span>
    </div>
    <ul class="contact">
      <li class="contact__item">
        <svg class="contact__icon" viewBox="0 0 24 24" aria-hidden="true">
          <path d="M6.6 3.5 L9.4 3 L11 7.6 L8.9 9.2 C9.9 11.5 12.4 14 14.8 15.1 L16.4 13 L21 14.6 L20.5 17.4 C20.3 18.6 19.2 19.5 18 19.4 C10.6 18.8 5.2 13.4 4.6 6 C4.5 4.8 5.4 3.7 6.6 3.5 Z" fill="none" stroke="currentColor" stroke-width="1.8" stroke-linejoin="round"/>
        </svg>
        <span>306-555-0187</span>
      </li>
      <li class="contact__item">
        <svg class="contact__icon" viewBox="0 0 24 24" aria-hidden="true">
          <circle cx="12" cy="12" r="10" fill="currentColor"/>
          <path d="M2 12 H22 M12 2 C8 6 8 18 12 22 M12 2 C16 6 16 18 12 22 M4 7 H20 M4 17 H20" fill="none" stroke="#ffffff" stroke-width="1.3"/>
        </svg>
        <span>www.LumaMove.ca</span>
      </li>
    </ul>
    <p class="holder-name">Marta</p>
  </section>

</main>
</body>
</html>
```